Sales PowerPoint Template to help us attract new customers

We need to create a generic PowerPoint template for our organization. We are in the commercial facilities industry, servicing convenience, restaurants, grocery, and retail customers in the US. We handle trades such as HVAC, Refrigeration, Plumbing, Electrical, Food Equipment, Coffee, etc.

We need to incorporate our new logo, updated colors, Font (Arial). We want it to stand out in this deck and avoid looking like all other facility companies. We want to make sure the template size is not too large (less than 20 MB), so it prevent people to edit/send.
Attached are new logo, colors, old powerpoint template, and finally the "New Design to Incorporate into Template" is new materials we're looking to leverage. This might give you ideas.

Create at least 10 slides (1 cover, 1 agenda slide, at least 7 general slides, and 1 wrap-up slide)

Target Market(s)

Convenience Stores, Retail Stores, Groceries, and Restaurants in the US

Industry/Entity Type

Facilities Services (HVAC, Refrigeration, Plumbing, Electrical, etc, repair and preventative maintenance)

Font styles to use
Other font styles liked:
• Arial

Requirements
Must have
• Follow company colors and font (Arial)
Should not have
• Not approved company colors, font

```html
<!DOCTYPE html>
<html lang="en">
<head>
<meta charset="utf-8">
<title>Sales Template – Slides 7 and 8</title>
<link href="https://fonts.googleapis.com/css2?family=Arimo:wght@400;700&family=Lato:wght@400&display=swap" rel="stylesheet">
<style>
  :root {
    --green: #819a2c;
    --sage: #dde0c0;
    --ink: #2e2e2e;
    --ink-soft: #3c3c3c;
    --label: #555555;
    --frame: #d6d6d6;
    --paper: #ffffff;
    --photo-a: #c9b79a;
    --photo-b: #6d6455;
  }
  * { margin: 0; padding: 0; box-sizing: border-box; }
  html, body { width: 960px; height: 1200px; overflow: hidden; background: var(--paper); }
  body { position: relative; font-family: Arimo, Arial, sans-serif; color: var(--ink); }

  .slide-note { position: absolute; left: 35px; font-family: Lato, Arial, sans-serif; font-size: 9px; line-height: 11.5px; color: var(--label); }
  .slide-note p + p { margin-top: 7px; }

  .slide { position: absolute; left: 336px; width: 472px; height: 264px; border: 1px solid var(--frame); background: var(--paper); overflow: hidden; }
  .slide-model { top: 105px; }
  .slide-scale { top: 424px; }

  .eyebrow { position: absolute; left: 21px; top: 20px; font-size: 10.5px; font-weight: 700; color: var(--ink-soft); letter-spacing: 0.1px; }
  .headline { position: absolute; left: 21px; top: 37px; font-size: 14.5px; line-height: 16.5px; font-weight: 700; color: var(--green); }

  .brand { position: absolute; left: 57px; top: 232px; display: flex; align-items: center; gap: 4px; }
  .brand-mark { width: 7px; height: 7px; background: var(--green); }
  .brand-name { font-size: 8px; font-weight: 400; letter-spacing: 1.6px; color: var(--green); line-height: 8px; }
  .brand-sub { position: absolute; left: 15px; top: 9px; font-size: 3.6px; color: var(--green); white-space: nowrap; letter-spacing: 0.1px; }

  .flow { position: absolute; left: 0; top: 0; }
  .flow-intro { position: absolute; left: 155px; top: 88px; width: 212px; text-align: center; font-size: 5.6px; line-height: 7.3px; font-weight: 700; color: var(--ink); }
  .flow-intro span { color: var(--ink-soft); }

  .step { position: absolute; top: 110px; width: 69px; height: 104px; background: var(--sage); padding: 0 7px; }
  .step-icon { position: absolute; left: 50%; top: 8px; transform: translateX(-50%); }
  .step-title { position: absolute; left: 7px; top: 42px; font-size: 5.2px; font-weight: 700; color: var(--ink-soft); }
  .step-text { position: absolute; left: 7px; top: 51px; width: 56px; font-size: 5px; line-height: 6.6px; color: var(--ink-soft); }
  .step-text b { color: var(--ink); }

  .scene-photo { position: absolute; left: 161px; top: 0; width: 138px; height: 264px; background: linear-gradient(135deg, var(--photo-a) 0%, #a3927a 45%, var(--photo-b) 100%); }
  .facts { position: absolute; left: 299px; top: 0; width: 173px; height: 264px; background: var(--sage); }
  .fact { position: absolute; left: 16px; width: 148px; font-size: 5.6px; line-height: 8.3px; font-weight: 700; color: var(--ink); }
  .fact span { font-weight: 700; color: var(--ink-soft); }
</style>
</head>
<body>

  <div class="slide-note" style="top:137px">
    <p>Slide 7 - Our Model</p>
    <p>Placeholder model graphic. To be<br>improved with more details.</p>
  </div>

  <section class="slide slide-model">
    <p class="eyebrow">our model</p>
    <h1 class="headline">The world’s first &lt;software name&gt;<br>integrated software suite</h1>

    <svg class="flow" width="472" height="264" viewBox="0 0 472 264" aria-hidden="true">
      <g fill="none" stroke="var(--green)" stroke-width="1.3">
        <polyline points="155,95 100.5,95 100.5,162 108,162"/>
        <polyline points="368,95 425.5,95 425.5,162 418,162"/>
      </g>
      <g fill="var(--green)">
        <polygon points="112,162 107,159.5 107,164.5"/>
        <polygon points="414,162 419,159.5 419,164.5"/>
      </g>
    </svg>
    <p class="flow-intro"><span>This text can be replaced with your own text.</span> Lorem ipsum dolor sit amet, consectetur adipiscing elit. Morbi dolor nisi, porttitor non volutpat vel,</p>

    <div class="step" style="left:113px">
      <svg class="step-icon" width="26" height="16" viewBox="0 0 26 16" aria-hidden="true">
        <path d="M5 14.5h16a4 4 0 0 0 .5-8 6 6 0 0 0-11.3-1.8A4.5 4.5 0 0 0 5 14.5z" fill="none" stroke="#555" stroke-width="0.7"/>
      </svg>
      <p class="step-title">Title to be changed</p>
      <p class="step-text">This text can be replaced with your own text. <b>Lorem ipsum dolor sit amet, consectetur adipiscing elit.</b></p>
    </div>

    <div class="step" style="left:191px">
      <svg class="step-icon" width="22" height="20" viewBox="0 0 22 20" aria-hidden="true">
        <g fill="none" stroke="#555" stroke-width="0.7">
          <rect x="2" y="11" width="3" height="7"/><rect x="7" y="7" width="3" height="11"/>
          <rect x="12" y="3" width="3" height="15"/><line x1="19" y1="1" x2="19" y2="18"/>
          <line x1="1" y1="18.5" x2="20" y2="18.5"/>
        </g>
      </svg>
      <p class="step-title">Title to be changed</p>
      <p class="step-text">This text can be replaced with your own text.</p>
    </div>

    <div class="step" style="left:269px">
      <svg class="step-icon" width="18" height="22" viewBox="0 0 18 22" aria-hidden="true">
        <g fill="none" stroke="#555" stroke-width="0.7">
          <ellipse cx="9" cy="3" rx="7.5" ry="2.2"/>
          <path d="M1.5 3v16c0 1.2 3.4 2.2 7.5 2.2s7.5-1 7.5-2.2V3"/>
          <path d="M1.5 8.3c0 1.2 3.4 2.2 7.5 2.2s7.5-1 7.5-2.2M1.5 13.6c0 1.2 3.4 2.2 7.5 2.2s7.5-1 7.5-2.2"/>
        </g>
      </svg>
      <p class="step-title">Title to be changed</p>
      <p class="step-text">This text can be replaced with your own text. <b>Lorem ipsum dolor sit amet, consectetur.</b></p>
    </div>

    <div class="step" style="left:348px">
      <svg class="step-icon" width="26" height="18" viewBox="0 0 26 18" aria-hidden="true">
        <g fill="none" stroke="#555" stroke-width="0.7">
          <circle cx="4" cy="2.5" r="1.5"/><path d="M2 6h4l-.6 6h-2.8z"/>
          <circle cx="10" cy="2.5" r="1.5"/><path d="M8 6h4l-.6 6h-2.8z"/>
          <circle cx="16" cy="2.5" r="1.5"/><path d="M14 6h4l-.6 6h-2.8z"/>
          <polyline points="3,16 9,10 13,13 24,4"/><polyline points="20,4 24,4 24,8"/>
        </g>
      </svg>
      <p class="step-title">Title to be changed</p>
      <p class="step-text">This text can be replaced with your own text. <b>Lorem ipsum.</b></p>
    </div>

    <div class="brand">
      <span class="brand-mark"></span>
      <span class="brand-name">NORVA</span>
      <span class="brand-sub">Facility Solutions</span>
    </div>
  </section>

  <div class="slide-note" style="top:449px">
    <p>Slide 8 - Scale</p>
  </div>

  <section class="slide slide-scale">
    <p class="eyebrow">our scale</p>
    <h1 class="headline">Every single<br>day of the<br>year…</h1>

    <div class="scene-photo" role="img" aria-label="Photo of a grocery checkout: a cashier scanning items for a family at the till"></div>

    <div class="facts">
      <p class="fact" style="top:29px"><span>We This text can be replaced with your own text.</span> Lorem ipsum dolor sit amet, consectetur adipiscing elit. Morbi dolor nisi, porttitor non volutpat vel, porta.</p>
      <p class="fact" style="top:74px"><span>We This text can be replaced with your own text.</span> Lorem ipsum dolor sit amet, consectetur adipiscing elit. Morbi dolor nisi.</p>
      <p class="fact" style="top:109px"><span>We This text can be replaced with your own text.</span> Lorem ipsum dolor.</p>
      <p class="fact" style="top:136px"><span>We This text can be replaced with your own text.</span> Lorem ipsum dolor sit amet, consectetur adipiscing elit. Morbi dolor nisi, porttitor non volutpat vel, porta.</p>
      <p class="fact" style="top:191px"><span>We This text can be replaced with your own text.</span> Lorem ipsum dolor sit amet, consectetur adipiscing elit.</p>
    </div>

    <div class="brand">
      <span class="brand-mark"></span>
      <span class="brand-name">NORVA</span>
      <span class="brand-sub">Facility Solutions</span>
    </div>
  </section>

</body>
</html>
```